Family Brewery needs a label design for the four different types of beer.

We need a label design for two beer bottle sizes (500 and 700 ml. )
The label design should include the family monogram and company logo, as it would be a corporate gift for the new year from our CEO to business partners and clients. We have one request for showing the company logo on bottle. As it would be the new year edition, we would like to see design "adaptive" in case we would like to keep it after the holidays on an ongoing basis. Our main company direction is design and manufacture of cooling equipment for ice rinks, so it would be fine but not necessary to see design related to our business (if you would like to check the company, there is our website - www.velmarik.ru)
Labels on bottles should be in the same style but vary depending on the variety and taste of beer.
Types of bear
-Pilzner ( 4.4 % of alcohol)
-Honig Pilsner(5.2 % of alcohol)
-Wiener Ale ( 4.7 % of alcohol)
-Weissbier (5.6 % of alcohol)
If you have any questions just message me and i will answer as soon as possible.
Files attached contain the family monogram, company logo ( velmarik ), picture of beer bottles that would be in usage.

```html
<!DOCTYPE html>
<html lang="en">
<head>
<meta charset="utf-8">
<title>Velmarik — New Year Beer Labels</title>
<link href="https://fonts.googleapis.com/css2?family=Roboto+Condensed:wght@300;400;500&display=swap" rel="stylesheet">
<style>
  :root {
    --bg: #ffffff;
    --ink: #ffffff;
    --pilzner: #e0404b;
    --honig: #3b9bc3;
    --wiener: #5d3a55;
    --weiss: #d98f7b;
    --neck-shade: rgba(0, 0, 0, 0.12);
  }
  * { margin: 0; padding: 0; box-sizing: border-box; }
  html, body {
    width: 1200px; height: 1000px; overflow: hidden;
    background: var(--bg);
    font-family: "Roboto Condensed", "Arial Narrow", sans-serif;
    color: var(--ink);
  }
  .canvas {
    position: relative; width: 1200px; height: 1000px;
    display: flex; justify-content: center; align-items: center; gap: 40px;
  }
  .label-set { display: flex; flex-direction: column; align-items: center; gap: 40px; }
  .neck-label {
    width: 250px; height: 64px;
    display: flex; align-items: center; justify-content: center; gap: 10px;
    background: var(--tone);
    box-shadow: inset 0 -6px 0 var(--neck-shade);
  }
  .neck-label .mark-dot {
    width: 18px; height: 18px; border-radius: 50%; border: 2px solid var(--ink);
  }
  .neck-label .brand { font-size: 18px; font-weight: 400; letter-spacing: 3px; text-transform: uppercase; }
  .body-label {
    position: relative; width: 250px; height: 360px;
    background: var(--tone); overflow: hidden;
  }
  .emblem-area {
    position: absolute; left: 14px; top: 28px; width: 176px; height: 176px;
    border-radius: 50%;
    background: radial-gradient(circle at 45% 45%, rgba(255,255,255,0.85), rgba(255,255,255,0.55));
  }
  .brand-vertical {
    position: absolute; left: 200px; top: 210px;
    transform: rotate(-90deg); transform-origin: left top;
    font-size: 30px; font-weight: 400; letter-spacing: 1px; white-space: nowrap;
  }
  .text-block {
    position: absolute; left: 14px; top: 228px; width: 160px;
  }
  .beer-name {
    font-size: 31px; font-weight: 400; letter-spacing: -0.5px; line-height: 1;
    white-space: nowrap;
  }
  .beer-style {
    margin-top: 10px;
    font-size: 22px; font-weight: 300; text-transform: uppercase; line-height: 1;
    white-space: nowrap;
  }
  .beer-number {
    position: absolute; right: 16px; top: 218px;
    font-size: 88px; font-weight: 500; line-height: 1;
  }
  .alc {
    position: absolute; left: 14px; bottom: 30px;
    font-size: 11px; font-weight: 400; letter-spacing: 0.5px;
  }
  .volume {
    position: absolute; right: 16px; bottom: 30px;
    font-size: 11px; font-weight: 400; letter-spacing: 0.5px;
  }
  .pilzner { --tone: var(--pilzner); }
  .honig { --tone: var(--honig); }
  .wiener { --tone: var(--wiener); }
  .weiss { --tone: var(--weiss); }
</style>
</head>
<body>
<main class="canvas">
  <section class="label-set pilzner">
    <div class="neck-label"><span class="mark-dot"></span><span class="brand">Velmarik</span></div>
    <div class="body-label">
      <div class="emblem-area" role="img" aria-label="Striped ice-sphere emblem"></div>
      <div class="brand-vertical">Velmarik</div>
      <div class="text-block">
        <div class="beer-name">BEER NAME</div>
        <div class="beer-style">Pilzner</div>
      </div>
      <div class="beer-number">1</div>
      <div class="alc">ALC 4.4 % BY VOL</div>
      <div class="volume">500 ML</div>
    </div>
  </section>
  <section class="label-set honig">
    <div class="neck-label"><span class="mark-dot"></span><span class="brand">Velmarik</span></div>
    <div class="body-label">
      <div class="emblem-area" role="img" aria-label="Striped ice-sphere emblem"></div>
      <div class="brand-vertical">Velmarik</div>
      <div class="text-block">
        <div class="beer-name">BEER NAME</div>
        <div class="beer-style">Honig Pilsner</div>
      </div>
      <div class="beer-number">2</div>
      <div class="alc">ALC 5.2 % BY VOL</div>
      <div class="volume">500 ML</div>
    </div>
  </section>
  <section class="label-set wiener">
    <div class="neck-label"><span class="mark-dot"></span><span class="brand">Velmarik</span></div>
    <div class="body-label">
      <div class="emblem-area" role="img" aria-label="Striped ice-sphere emblem"></div>
      <div class="brand-vertical">Velmarik</div>
      <div class="text-block">
        <div class="beer-name">BEER NAME</div>
        <div class="beer-style">Wiener Ale</div>
      </div>
      <div class="beer-number">3</div>
      <div class="alc">ALC 4.7 % BY VOL</div>
      <div class="volume">500 ML</div>
    </div>
  </section>
  <section class="label-set weiss">
    <div class="neck-label"><span class="mark-dot"></span><span class="brand">Velmarik</span></div>
    <div class="body-label">
      <div class="emblem-area" role="img" aria-label="Striped ice-sphere emblem"></div>
      <div class="brand-vertical">Velmarik</div>
      <div class="text-block">
        <div class="beer-name">BEER NAME</div>
        <div class="beer-style">Weissbier</div>
      </div>
      <div class="beer-number">4</div>
      <div class="alc">ALC 5.6 % BY VOL</div>
      <div class="volume">500 ML</div>
    </div>
  </section>
</main>
</body>
</html>
```